Re design current site.

Redesign of the current site. Like current design But I don't own it so I need a custom design similar to the current one. Want the model pictures to be shown off as they currently do on the home page I want to show off contact info make it very noticeable and readable.
Target Market(s)
Males age 30-60
Number of Pages Required
1 page
Requirements
Must have
- Must show off model pictures on the page. Must show contact info easy to read easy to find.

```html
<!DOCTYPE html>
<html lang="en">
<head>
<meta charset="utf-8">
<title>Velvet Lane Models</title>
<link rel="stylesheet" href="https://fonts.googleapis.com/css2?family=Gelasio:wght@400;700&family=Roboto+Condensed:wght@400;700&family=Arimo:wght@400&display=swap">
<style>
:root{
  --bg-deep:#2a0304;
  --bg-mid:#5e0a0c;
  --red:#d01010;
  --red-dark:#8f0606;
  --coral:#e2625f;
  --field:#f3adaf;
  --field-text:#a04040;
  --title-red:#c8231e;
  --ink:#555;
  --pink:#f6dde3;
  --white:#fff;
  --gold:#e7b12b;
  --green:#6c9a2c;
  --blue:#2aa3d4;
}
*{margin:0;padding:0;box-sizing:border-box}
html,body{width:733px;height:1200px;overflow:hidden}
body{position:relative;background:radial-gradient(ellipse at 50% 45%,var(--bg-mid) 0%,#430607 55%,var(--bg-deep) 100%);font-family:"Gelasio",serif;color:var(--ink)}
.abs{position:absolute}
.top-ornament{left:219px;top:24px;width:296px;height:40px;background:linear-gradient(90deg,rgba(230,20,20,.0),rgba(230,20,20,.75) 20%,rgba(230,20,20,.75) 80%,rgba(230,20,20,0));border-radius:20px}
.brand{left:266px;top:78px;width:230px;text-align:left}
.brand-name{display:flex;align-items:center;gap:7px;font-family:"Gelasio",serif;font-weight:400;font-size:19px;color:var(--white);letter-spacing:.5px}
.brand-dot{width:12px;height:12px;border-radius:50%;background:var(--red)}
.brand-tag{margin-top:6px;font-size:8.6px;font-weight:700;color:var(--white);letter-spacing:.1px}
.badge-seal{left:497px;top:78px;width:46px;height:46px;border-radius:50%;background:radial-gradient(circle,#f6d15a,var(--gold) 60%,#a87812)}
.badge-shield{left:553px;top:78px;width:46px;height:48px;background:linear-gradient(#9ccb48,var(--green));clip-path:polygon(0 10%,50% 0,100% 10%,100% 55%,50% 100%,0 55%)}
.panel{left:103px;top:131px;width:523px;height:972px;background:var(--white)}
.nav{left:0;top:0;width:523px;height:29px;background:linear-gradient(#f01a14,var(--red) 50%,var(--red-dark));display:flex;justify-content:center;align-items:center;gap:13px;border-bottom:3px solid #e8463c}
.nav a{font-size:9.2px;color:var(--white);text-decoration:none}
.nav-arrow{top:8px}
.hero{left:0;top:29px;width:523px;height:233px;background:linear-gradient(100deg,#3c3a3a 0%,#1e1d1d 45%,#5d3422 70%,#2a1a14 100%)}
.contact{left:327px;top:37px;width:171px;height:220px;background:var(--coral);text-align:center;color:var(--white)}
.contact h2{margin-top:9px;font-family:"Roboto Condensed",sans-serif;font-weight:700;font-size:14px;line-height:1}
.contact .sub{font-family:"Roboto Condensed",sans-serif;font-size:5.6px;font-weight:700}
.contact .line{font-family:"Roboto Condensed",sans-serif;font-size:8.3px;font-weight:700;color:#fff;margin-top:3px;line-height:1.3}
.contact .line+.line{margin-top:0}
.fields{margin:8px auto 0;width:120px;display:flex;flex-direction:column;gap:5px}
.row{display:flex;gap:4px}
.field{height:16px;background:var(--field);font-family:"Arimo",sans-serif;font-size:5.2px;color:var(--field-text);text-align:left;padding:5px 4px;position:relative;flex:1}
.field.sel::after{content:"";position:absolute;right:4px;top:7px;border:2px solid transparent;border-top-color:var(--field-text)}
.cta-band{left:319px;top:200px;width:186px;height:37px;background:var(--white);box-shadow:0 1px 3px rgba(0,0,0,.3)}
.cta{left:345px;top:208px;width:135px;height:21px;background:linear-gradient(#e85a55,#d8403b);color:#fff;font-family:"Roboto Condensed",sans-serif;font-size:10.5px;display:flex;align-items:center;justify-content:center;gap:4px}
.cta-dot{width:9px;height:9px;border-radius:50%;background:#2a0a0a;display:flex;align-items:center;justify-content:center}
.terms{left:327px;top:243px;width:171px;text-align:center;font-size:4.2px;font-style:italic;color:#fff}
.intro{left:0;top:262px;width:523px;height:380px;background:linear-gradient(var(--pink),var(--white))}
.intro h1{position:absolute;top:27px;width:100%;text-align:center;font-size:15.5px;font-weight:700;color:var(--title-red)}
.intro p{position:absolute;left:98px;top:46px;width:350px;text-align:center;font-size:7.8px;line-height:11.6px;color:var(--ink)}
.intro p b{color:#444}
.step{position:absolute;top:101px;width:120px;text-align:center}
.step h3{font-weight:400;font-size:13px;color:#555;margin-top:1px;line-height:1.1}
.step span{font-size:6.4px;color:#666}
.divider{position:absolute;top:194px;width:100%;text-align:center;font-size:13px;font-weight:700;color:#666}
.flourish{position:absolute;top:200px;width:55px;height:6px;border-radius:3px;background:linear-gradient(90deg,rgba(232,140,140,0),#e8a0a0)}
.card{position:absolute;width:110px;height:123px;border:1px solid #ddd;background:#fff}
.card .photo{position:absolute;left:6px;top:6px;width:97px;height:107px}
.name{position:absolute;width:110px;text-align:center;font-family:"Arimo",sans-serif;font-size:7.6px;color:#222}
.stats{position:absolute;width:110px;text-align:center;font-size:4.6px;color:#444}
.tone-a{background:linear-gradient(#d2a79f,#c3246e)}
.tone-b{background:linear-gradient(#9b8272,#e9d7cf)}
.tone-c{background:linear-gradient(#6b8a3c,#c9b9b7)}
.tone-d{background:linear-gradient(#3a4552,#6f6570)}
.tone-e{background:linear-gradient(#4a3a3a,#d03440)}
.tone-f{background:linear-gradient(#1a1a1a,#3a1e1e)}
.foot-brand{left:266px;top:1124px;width:200px;display:flex;justify-content:center;align-items:center;gap:6px;font-size:16px;color:#fff}
.copy{left:0;top:1149px;width:733px;text-align:center;font-size:10.5px;font-weight:700;color:#fff}
</style>
</head>
<body>
<div class="abs top-ornament" role="img" aria-label="Red scroll ornament"></div>
<div class="abs brand">
  <div class="brand-name"><span class="brand-dot"></span>VELVET LANE MODELS</div>
  <div class="brand-tag">TREAT YOURSELF AND WE'LL TREAT YOU</div>
</div>
<div class="abs badge-seal"></div>
<div class="abs badge-shield"></div>

<div class="abs panel">
  <nav class="abs nav">
    <a href="#">Home</a><a href="#">About Us</a><a href="#">Booking</a><a href="#">Rates</a><a href="#">Models</a><a href="#">Employment</a><a href="#">Links</a>
  </nav>
  <svg class="abs nav-arrow" style="left:6px" width="12" height="10" viewBox="0 0 12 10"><path d="M0 5h9M6 1l4 4-4 4" stroke="#f2a22c" stroke-width="2" fill="none"/></svg>
  <svg class="abs nav-arrow" style="left:505px" width="12" height="10" viewBox="0 0 12 10"><path d="M12 5H3M6 1L2 5l4 4" stroke="#f2a22c" stroke-width="2" fill="none"/></svg>

  <div class="abs hero" role="img" aria-label="Photo of a couple seated on chairs, man in suit and woman in red heels"></div>

  <div class="abs contact">
    <h2>CONTACT US NOW!</h2>
    <div class="sub">Your perfect match is just a click away</div>
    <div class="line">Email: book@velvetlanemodels.com</div>
    <div class="line">Phone: 555-013-4827</div>
    <div class="fields">
      <div class="field sel">Choose model</div>
      <div class="row"><div class="field sel" style="flex:2.2">Month</div><div class="field sel">Day</div><div class="field sel">Year</div></div>
      <div class="field sel">Appointment city</div>
      <div class="field">Full name</div>
      <div class="field">Phone</div>
    </div>
  </div>
  <div class="abs cta-band"></div>
  <div class="abs cta">REQUEST APPOINTMENT <span class="cta-dot"><svg width="5" height="5" viewBox="0 0 5 5"><path d="M1 0l3 2.5L1 5" fill="#fff"/></svg></span></div>
  <div class="abs terms">By signing up you agree to our Terms and Privacy Policy</div>

  <section class="abs intro">
    <h1>REQUEST FOR A MODEL</h1>
    <p><b>VelvetLane Concierge Service</b> allows clients to request VelvetLane to search for models in the location you plan on traveling to. We will search and find attractive models for the dates requested. We also verify they are interested in the service you expect/request and that the pictures we have are recent and real.</p>

    <div class="step" style="left:78px">
      <svg width="34" height="34" viewBox="0 0 34 34"><path d="M17 30C4 20 3 13 6 9c3-4 8-3 11 1 3-4 8-5 11-1 3 4 2 11-11 21z" fill="#e2625f"/><circle cx="26" cy="6" r="2.5" fill="#2aa3d4"/><circle cx="29" cy="27" r="2" fill="#2aa3d4"/></svg>
      <h3>REQUEST</h3><span>Request a free appointment</span>
    </div>
    <div class="step" style="left:204px">
      <svg width="34" height="34" viewBox="0 0 34 34"><circle cx="17" cy="11" r="8" fill="none" stroke="#e2625f" stroke-width="3"/><path d="M17 19v14M11 27h12" stroke="#e2625f" stroke-width="3"/></svg>
      <h3>CHOOSE</h3><span>Choose your preferred model</span>
    </div>
    <div class="step" style="left:334px">
      <svg width="34" height="34" viewBox="0 0 34 34"><circle cx="12" cy="14" r="5" fill="#2aa3d4"/><path d="M2 32c0-8 4-11 10-11s10 3 10 11z" fill="#2aa3d4"/><circle cx="23" cy="15" r="4" fill="#e2625f"/><path d="M16 32c0-7 3-10 7-10s8 3 8 10z" fill="#e2625f"/><circle cx="25" cy="5" r="2.5" fill="#e2625f"/></svg>
      <h3>MEET</h3><span>Meet your preferred model</span>
    </div>

    <div class="flourish" role="img" aria-label="Left decorative flourish" style="left:176px"></div>
    <div class="divider">Models</div>
    <div class="flourish" role="img" aria-label="Right decorative flourish" style="left:292px;transform:scaleX(-1)"></div>
  </section>

  <div class="card" style="left:32px;top:494px"><div class="photo tone-a" role="img" aria-label="Model photo: Ivy"></div></div>
  <div class="card" style="left:148px;top:494px"><div class="photo tone-b" role="img" aria-label="Model photo: Brooke"></div></div>
  <div class="card" style="left:264px;top:494px"><div class="photo tone-a" role="img" aria-label="Model photo: Ivy"></div></div>
  <div class="card" style="left:381px;top:494px"><div class="photo tone-b" role="img" aria-label="Model photo: Brooke"></div></div>
  <div class="name" style="left:32px;top:622px">IVY</div><div class="stats" style="left:32px;top:632px">20 - 5'3 - 120 - 34B</div>
  <div class="name" style="left:148px;top:622px">BROOKE</div><div class="stats" style="left:148px;top:632px">20 - 5'3 - 120 - 34B</div>
  <div class="name" style="left:264px;top:622px">IVY</div><div class="stats" style="left:264px;top:632px">20 - 5'3 - 120 - 34B</div>
  <div class="name" style="left:381px;top:622px">BROOKE</div><div class="stats" style="left:381px;top:632px">20 - 5'3 - 120 - 34B</div>

  <div class="card" style="left:32px;top:642px"><div class="photo tone-c" role="img" aria-label="Model photo: Lola Grace"></div></div>
  <div class="card" style="left:148px;top:642px"><div class="photo tone-d" role="img" aria-label="Model photo: Jade"></div></div>
  <div class="card" style="left:264px;top:642px"><div class="photo tone-c" role="img" aria-label="Model photo: Lola Grace"></div></div>
  <div class="card" style="left:381px;top:642px"><div class="photo tone-d" role="img" aria-label="Model photo: Jade"></div></div>
  <div class="name" style="left:32px;top:770px">LOLA GRACE</div><div class="stats" style="left:32px;top:780px">20 - 5'3 - 120 - 34B</div>
  <div class="name" style="left:148px;top:770px">JADE</div><div class="stats" style="left:148px;top:780px">20 - 5'3 - 120 - 34B</div>
  <div class="name" style="left:264px;top:770px">LOLA GRACE</div><div class="stats" style="left:264px;top:780px">20 - 5'3 - 120 - 34B</div>
  <div class="name" style="left:381px;top:770px">JADE</div><div class="stats" style="left:381px;top:780px">20 - 5'3 - 120 - 34B</div>

  <div class="card" style="left:32px;top:790px"><div class="photo tone-e" role="img" aria-label="Model photo: Skye"></div></div>
  <div class="card" style="left:148px;top:790px"><div class="photo tone-f" role="img" aria-label="Model photo: Nina Belle"></div></div>
  <div class="card" style="left:264px;top:790px"><div class="photo tone-e" role="img" aria-label="Model photo: Skye"></div></div>
  <div class="card" style="left:381px;top:790px"><div class="photo tone-f" role="img" aria-label="Model photo: Nina Belle"></div></div>
  <div class="name" style="left:32px;top:918px">SKYE</div><div class="stats" style="left:32px;top:928px">20 - 5'3 - 120 - 34B</div>
  <div class="name" style="left:148px;top:918px">NINA BELLE</div><div class="stats" style="left:148px;top:928px">20 - 5'3 - 120 - 34B</div>
  <div class="name" style="left:264px;top:918px">SKYE</div><div class="stats" style="left:264px;top:928px">20 - 5'3 - 120 - 34B</div>
  <div class="name" style="left:381px;top:918px">NINA BELLE</div><div class="stats" style="left:381px;top:928px">20 - 5'3 - 120 - 34B</div>
</div>

<div class="abs foot-brand"><span class="brand-dot"></span>VELVET LANE MODELS</div>
<div class="abs copy">Copyright 2017. All rights reserved</div>
</body>
</html>
```